Larkhaven Institute by graduating students from college in two years

Based on the logo design, create stationary and business cards for
Dr. Velmor T Quenby, CEO, (555) 412-3076
and Lorna Pettigrew, Respresentative, (555) 238-6041
Address: 4197 Thistlemoor Lane, Brindlewood Station, VA 20517
Incorporate elelments of the logo

Target Market(s)

USA

Font styles to use
Other font styles liked:
• match with the logo type style

```html
<!DOCTYPE html>
<html lang="en">
<head>
<meta charset="utf-8">
<title>Larkhaven Institute Letterhead</title>
<link href="https://fonts.googleapis.com/css2?family=Arimo:wght@400;700&family=Montserrat:wght@600;700&display=swap" rel="stylesheet">
<style>
  :root {
    --navy: #0c2260;
    --gold: #f5bf2a;
    --paper: #ffffff;
    --backdrop: #b9b9b9;
    --ink: #4a4a4a;
    --ink-soft: #5a5a5a;
    --signature-tone: #d9dbe0;
  }
  * { box-sizing: border-box; margin: 0; padding: 0; }
  html, body { width: 1200px; height: 1159px; overflow: hidden; }
  body { background: var(--backdrop); position: relative; font-family: "Arimo", Arial, sans-serif; }

  .letterhead {
    position: absolute; left: 185px; top: 30px;
    width: 830px; height: 1100px;
    background: var(--paper);
    box-shadow: 0 6px 24px rgba(0,0,0,.25);
    overflow: hidden;
  }
  .header-band { position: absolute; left: 0; top: 0; width: 830px; height: 120px; }

  .brand-seal {
    position: absolute; left: 24px; top: 22px;
    width: 150px; height: 150px; border-radius: 50%;
    background: var(--paper);
    border: 5px solid var(--gold);
    display: flex; align-items: center; justify-content: center;
    text-align: center; padding: 14px;
  }
  .brand-name { font-family: "Arimo", Arial, sans-serif; font-weight: 700; font-size: 17px; line-height: 1.2; color: var(--navy); }

  .contact { position: absolute; color: #fff; font-size: 13px; line-height: 1.25; }
  .contact .person { color: var(--gold); font-weight: 700; font-size: 16px; }
  .contact .phone-icon { display: inline-block; width: 11px; height: 11px; vertical-align: -1px; margin-right: 4px; }
  .contact-ceo { left: 250px; top: 18px; }
  .contact-rep { left: 470px; top: 18px; }
  .contact-address { left: 640px; top: 20px; }
  .divider { position: absolute; top: 14px; width: 2px; height: 54px; background: var(--gold); transform: skewX(-18deg); }
  .divider-one { left: 438px; }
  .divider-two { left: 612px; }

  .letter-body { position: absolute; left: 110px; top: 300px; width: 610px; color: var(--ink); }
  .salutation { font-family: "Montserrat", sans-serif; font-weight: 700; font-size: 17px; color: var(--ink); margin-bottom: 22px; }
  .letter-body p { font-size: 14px; line-height: 18px; color: var(--ink-soft); margin-bottom: 20px; }
  .closing { font-family: "Montserrat", sans-serif; font-weight: 700; font-size: 11px; color: var(--ink); margin-top: 30px; }
  .signature-area { width: 150px; height: 46px; margin-top: 22px; border-radius: 6px; background: linear-gradient(90deg, var(--signature-tone), #eef0f3); }
</style>
</head>
<body>
  <main class="letterhead">
    <svg class="header-band" viewBox="0 0 830 120" aria-hidden="true">
      <polygon points="0,0 830,0 830,70 0,110" fill="var(--navy)"/>
      <polygon points="0,110 830,70 830,75 0,116" fill="var(--gold)"/>
    </svg>

    <div class="brand-seal"><span class="brand-name">Larkhaven Institute</span></div>

    <div class="contact contact-ceo">
      <div class="person">Dr. Velmor T Quenby</div>
      <div>CEO</div>
      <div><svg class="phone-icon" viewBox="0 0 12 12"><path d="M1 4c0-2 2-3 5-3s5 1 5 3l-2 1-1-1H4L3 5zM3 6h6l2 5H1z" fill="#fff"/></svg>(555) 412-3076</div>
    </div>
    <span class="divider divider-one"></span>
    <div class="contact contact-rep">
      <div class="person">Lorna Pettigrew</div>
      <div>Respresentative</div>
      <div><svg class="phone-icon" viewBox="0 0 12 12"><path d="M1 4c0-2 2-3 5-3s5 1 5 3l-2 1-1-1H4L3 5zM3 6h6l2 5H1z" fill="#fff"/></svg>(555) 238-6041</div>
    </div>
    <span class="divider divider-two"></span>
    <div class="contact contact-address">
      <div>4197 Thistlemoor Lane</div>
      <div>Brindlewood Station</div>
      <div>VA 20517</div>
    </div>

    <section class="letter-body">
      <h1 class="salutation">Dear Mr. Halloway,</h1>
      <p>Lorem ipsum dolor sit amet, consectetuer adipiscing elit, sed diam nonmmy nibh euismod tincidunt ut laor eet dolore magna aliquam erat volutpat. Ut wisi enim ad minim veniam, quis nostrud exerci tationmcorper suscipit lobortis nisl ut aliquip ex ea commodo consequat. Duis autem vel eum iriure dolor in hendrerit in vulputate velit esse molestie consequat, vel illum dolore eu feugiat</p>
      <p>Rorem ipsum dolor sit amet, consectetuer adipiscing elit, sed diam nonmmy nibh euismod tincidunt ut laor eet dolore magna aliquam erat volutpat. Ut wisi enim ad minim veniam, quis nostrud exerci tationmcorper suscipit lobortis nisl ut aliquip ex ea commodo consequat. Duis autem vel eum iriure dolor in hendrerit in vulputate velit esse molest</p>
      <p>Dorem ipsum dolor sit amet, consectetuer adipiscing elit, sed diam nonmmy nibh euismod tincidunt ut laor eet dolore magna aliquam erat volutpat. Ut wisi enim ad minim veniam, quis nostrud exerci tationmcorper suscipit lobortis nisl ut aliquip ex ea commodo consequat. Duis autem vel eum iriure dolor in hendrerit in suscipit lobortis nisl ut aliquip ex ea commodo consequat. Duis autem vel eum iriure dolor in hendrerit in vulputate velit esse molestie consequat, vel illum</p>
      <p>Sorem ipsum dolor sit amet, consectetuer adipiscing elit, sed diam nonmmy nibh euismod tincidunt ut laor eet dolore magna aliquam erat volutpat. Ut wisi enim ad minim veniam, quis nostrud exerci tationmcorper suscipit lobortis nisl ut aliquip ex ea commodo consequat. Duis autem vel eum iriure dolor in</p>
      <div class="closing">Sincerely,</div>
      <div class="signature-area" role="img" aria-label="Handwritten signature of the sender"></div>
    </section>
  </main>
</body>
</html>
```